Need a business letterhead for word docs

Hi, I need a business letterhead. We have had some before but they have issues printing them. I have attached a sample of what we have used that I want improved :) and a PSD of our logo, please use the one with all caps. This will be used for all our correspondance with clients and profeesionals. Our client base are children, so these documents will go to their parents and doctors and paediatricians who also treat these children.

Target Market(s)

Clients (who are families and children) and doctors/paediatricians

Industry/Entity Type

Health Care

Font styles to use
Sans Serif

Colors
85cae6

Requirements
Must have
• My logo and the feel of my logo
Nice to have
• clean feel

```html
<!DOCTYPE html>
<html lang="en">
<head>
<meta charset="utf-8">
<title>Tenderoak Letterhead</title>
<link href="https://fonts.googleapis.com/css2?family=Arimo:ital,wght@0,400;0,700;1,700&display=swap" rel="stylesheet">
<style>
  :root {
    --brand-blue: #29b4e6;
    --brand-soft: #85cae6;
    --ink: #111111;
    --link: #1a1aff;
    --rule: #c9c9c9;
    --paper: #ffffff;
  }
  * { margin: 0; padding: 0; box-sizing: border-box; }
  html, body { width: 843px; height: 1200px; overflow: hidden; background: var(--paper); }
  body { font-family: "Arimo", Arial, sans-serif; color: var(--ink); }

  .letterhead { position: relative; width: 843px; height: 1200px; background: var(--paper); }

  .brand {
    position: absolute;
    display: flex;
    align-items: center;
    gap: 10px;
  }
  .brand-dot {
    width: 18px; height: 18px;
    border-radius: 50%;
    background: var(--brand-soft);
  }
  .brand-name {
    font-size: 22px;
    font-weight: 400;
    color: var(--brand-blue);
    white-space: nowrap;
  }
  .brand--header { left: 50px; top: 80px; }
  .brand--footer { left: 50px; top: 1098px; }

  .tagline {
    position: absolute;
    right: 38px;
    top: 81px;
    font-size: 17px;
    font-weight: 700;
    font-style: italic;
    white-space: nowrap;
  }

  .contact { position: absolute; top: 1134px; font-size: 13.5px; line-height: 24px; white-space: nowrap; }
  .contact-label { color: var(--brand-blue); font-weight: 700; margin-right: 6px; }
  .contact-label--light { font-weight: 400; margin-right: 2px; }
  .contact--addresses { left: 39px; }
  .contact--reach { left: 353px; }
  .contact a { color: var(--link); text-decoration: underline; }
  .contact a.web { font-weight: 700; }
  .contact .spacer { display: inline-block; width: 8px; }

  .footer-divider {
    position: absolute;
    left: 317px; top: 1109px;
    width: 1px; height: 73px;
    background: var(--rule);
  }
</style>
</head>
<body>
  <main class="letterhead">
    <header>
      <div class="brand brand--header">
        <span class="brand-dot"></span>
        <span class="brand-name">Tenderoak</span>
      </div>
      <p class="tagline">Caring For Growing Families</p>
    </header>

    <footer>
      <div class="brand brand--footer">
        <span class="brand-dot"></span>
        <span class="brand-name">Tenderoak</span>
      </div>
      <div class="contact contact--addresses">
        <p><span class="contact-label">A:</span>48 Linden Grove, Hampton 3188</p>
        <p><span class="contact-label">A:</span>15 Ashby Street, Elsternwick 3185</p>
      </div>
      <div class="footer-divider"></div>
      <div class="contact contact--reach">
        <p><span class="contact-label contact-label--light">P:</span>03 9000 4127</p>
        <p><span class="contact-label">E:</span><a href="mailto:hello@tenderoakclinic.com.au">hello@tenderoakclinic.com.au</a><span class="spacer"></span><span class="contact-label">W:</span><a class="web" href="#">www.tenderoakclinic.com.au</a></p>
      </div>
    </footer>
  </main>
</body>
</html>
```